Harbor Portable Scanning business cards / stationary
President CEO
Harbor Portable Scanning business cards / stationary - Health
Creative Brief
Professional
Lena Marcovici
P.O. Box 527 Ashwick NJ 08176
Info@harborportablescanninginc.com
www.harborportablescanninginc.com
I need business cards and stationary
I would like to see a version with my logo also on the back

```html
<!DOCTYPE html>
<html lang="en">
<head>
<meta charset="utf-8">
<title>Harbor Portable Scanning – Stationery</title>
<link href="https://fonts.googleapis.com/css2?family=Open+Sans:wght@400;600;700&display=swap" rel="stylesheet">
<style>
:root{
  --bg:#2c3136;
  --paper:#ffffff;
  --blue:#1f78cf;
  --blue-dark:#0d4f9c;
  --blue-light:#6cb8ee;
  --ink:#4a4f55;
  --rule:#b9bec4;
}
*{box-sizing:border-box;margin:0;padding:0}
html,body{width:1200px;height:602px;overflow:hidden}
body{background:var(--bg);font-family:"Open Sans",Arial,sans-serif;color:var(--ink);position:relative}
.sheet{position:absolute;background:var(--paper);box-shadow:0 3px 10px rgba(0,0,0,.45);overflow:hidden}
.wave{position:absolute;left:0;width:100%;display:block}
.wave-bottom{bottom:0}
.wave-top{top:0}
.brand{display:flex;align-items:center;gap:8px;position:absolute}
.brand-dot{border-radius:50%;border:3px solid var(--blue);flex:none}
.brand-name{color:var(--blue);font-weight:700;text-transform:uppercase;letter-spacing:.06em;line-height:1.1}
.brand.on-blue .brand-dot{border-color:#fff}
.brand.on-blue .brand-name{color:#fff}
.footer-text{position:absolute;color:#fff;font-size:6px;line-height:1.5}

/* business cards */
.card{width:178px;height:105px;border-radius:3px}
.card-front{left:68px;top:26px}
.card-back{left:68px;top:178px;background:linear-gradient(180deg,#2f8ad9,var(--blue-dark))}
.card-front .brand{left:12px;top:10px}
.card-front .brand-dot{width:22px;height:22px;border-width:2px}
.card-front .brand-name{font-size:8px}
.card-person{position:absolute;right:10px;top:63px;text-align:right;color:#fff;font-size:5.5px;line-height:1.35;z-index:2}
.card-person strong{font-size:7px;font-weight:600;display:block}
.card-contact{position:absolute;left:10px;bottom:6px;color:#fff;font-size:4.5px;line-height:1.4;z-index:2}
.card-back .brand{left:40px;top:30px}
.card-back .brand-dot{width:30px;height:30px;border-width:3px}
.card-back .brand-name{font-size:9px}
.card-back .card-web{position:absolute;left:0;right:0;bottom:12px;text-align:center;color:#fff;font-size:5px}

/* letterhead */
.letterhead{left:271px;top:16px;width:440px;height:572px}
.letterhead .brand{left:36px;top:36px}
.letterhead .brand-dot{width:44px;height:44px;border-width:4px}
.letterhead .brand-name{font-size:14px}

/* fax */
.fax{left:748px;top:16px;width:426px;height:572px}
.fax .brand{left:30px;top:36px}
.fax .brand-dot{width:44px;height:44px;border-width:4px}
.fax .brand-name{font-size:14px}
.fax-title{position:absolute;left:30px;top:128px;font-size:40px;font-weight:400;color:#333}
.fax-table{position:absolute;left:30px;top:184px;width:366px;border-collapse:collapse;font-size:6px}
.fax-table td{border:1px solid var(--rule);height:12px;padding:0 3px;vertical-align:middle}
.fax-table td.label{width:40px}
.fax-checks{position:absolute;left:30px;top:254px;width:366px;display:flex;justify-content:space-between;font-size:6px}
.fax-checks span::before{content:"";display:inline-block;width:5px;height:5px;border:1px solid var(--ink);margin-right:3px;vertical-align:-1px}
.fax-rule{position:absolute;left:30px;top:266px;width:366px;border-top:1px solid var(--rule)}
.fax-comments{position:absolute;left:30px;top:272px;font-size:6px}

/* envelope */
.envelope{left:58px;top:346px;width:482px;height:242px}
.envelope .brand{left:24px;top:70px}
.envelope .brand-dot{width:46px;height:46px;border-width:4px}
.envelope .brand-name{font-size:14px}
.envelope-return{position:absolute;left:120px;top:31px;color:#fff;font-size:6px;letter-spacing:.05em}
.envelope-address{position:absolute;left:24px;top:132px;font-size:6px;line-height:1.6;color:var(--ink)}
.envelope-window{position:absolute;left:24px;top:188px;width:132px;height:34px;border:1px solid #d3d7db;border-radius:4px;background:#f6f7f8}

/* notepad */
.notepad{left:569px;top:272px;width:170px;height:316px}
.notepad .brand{left:14px;top:18px}
.notepad .brand-dot{width:22px;height:22px;border-width:2px}
.notepad .brand-name{font-size:7px}
.note-lines{position:absolute;left:20px;right:20px;top:66px;height:170px;background:repeating-linear-gradient(180deg,transparent 0 9px,#8a9096 9px 10px)}
.note-date{position:absolute;right:22px;top:252px;font-size:6px}
.note-date::after{content:"";display:inline-block;width:34px;border-bottom:1px solid var(--ink);margin-left:3px}
</style>
</head>
<body>

<!-- letterhead -->
<section class="sheet letterhead" aria-label="Letterhead">
  <div class="brand"><span class="brand-dot"></span><span class="brand-name">Harbor<br>Portable Scanning</span></div>
  <svg class="wave wave-bottom" viewBox="0 0 440 70" height="70" preserveAspectRatio="none" aria-hidden="true">
    <path d="M0 22 C120 0 260 40 440 8 L440 70 L0 70Z" fill="var(--blue-light)"/>
    <path d="M0 34 C140 12 280 52 440 22 L440 70 L0 70Z" fill="var(--blue)"/>
    <path d="M0 48 C150 34 300 62 440 40 L440 70 L0 70Z" fill="var(--blue-dark)"/>
  </svg>
  <p class="footer-text" style="left:30px;bottom:10px">P.O. Box 527 Ashwick NJ 08176<br>Phone: 856-555-0142 &nbsp; Fax: 856-555-0143</p>
  <p class="footer-text" style="right:30px;bottom:10px">www.harborportablescanninginc.com</p>
</section>

<!-- fax -->
<section class="sheet fax" aria-label="Fax cover sheet">
  <div class="brand"><span class="brand-dot"></span><span class="brand-name">Harbor<br>Portable Scanning</span></div>
  <h1 class="fax-title">Fax</h1>
  <table class="fax-table">
    <tr><td class="label">To:</td><td></td><td class="label">From:</td><td></td></tr>
    <tr><td class="label">Fax:</td><td></td><td class="label">Pages:</td><td></td></tr>
    <tr><td class="label">Phone:</td><td></td><td class="label">Date:</td><td></td></tr>
    <tr><td class="label">Re:</td><td></td><td class="label">CC:</td><td></td></tr>
  </table>
  <div class="fax-checks"><span>Urgent</span><span>For Review</span><span>Please Comment</span><span>Please Reply</span><span>Please Recycle</span></div>
  <div class="fax-rule"></div>
  <p class="fax-comments">Comments:</p>
  <svg class="wave wave-bottom" viewBox="0 0 426 70" height="70" preserveAspectRatio="none" aria-hidden="true">
    <path d="M0 22 C120 0 250 40 426 8 L426 70 L0 70Z" fill="var(--blue-light)"/>
    <path d="M0 34 C130 12 270 52 426 22 L426 70 L0 70Z" fill="var(--blue)"/>
    <path d="M0 48 C140 34 290 62 426 40 L426 70 L0 70Z" fill="var(--blue-dark)"/>
  </svg>
  <p class="footer-text" style="left:30px;bottom:10px">P.O. Box 527 Ashwick NJ 08176<br>Info@harborportablescanninginc.com</p>
  <p class="footer-text" style="right:30px;bottom:10px">www.harborportablescanninginc.com</p>
</section>

<!-- business card front -->
<section class="sheet card card-front" aria-label="Business card front">
  <div class="brand"><span class="brand-dot"></span><span class="brand-name">Harbor<br>Portable Scanning</span></div>
  <svg class="wave wave-bottom" viewBox="0 0 178 62" height="62" preserveAspectRatio="none" aria-hidden="true">
    <path d="M0 12 C60 0 110 20 178 2 L178 62 L0 62Z" fill="var(--blue-light)"/>
    <path d="M0 18 C60 6 120 26 178 10 L178 62 L0 62Z" fill="var(--blue)"/>
    <path d="M0 40 C70 30 120 50 178 36 L178 62 L0 62Z" fill="var(--blue-dark)"/>
  </svg>
  <p class="card-person"><strong>Lena Marcovici</strong>President CEO</p>
  <p class="card-contact">P.O. Box 527 Ashwick NJ 08176 · Phone: 856-555-0142<br>Info@harborportablescanninginc.com</p>
</section>

<!-- business card back -->
<section class="sheet card card-back" aria-label="Business card back">
  <svg class="wave wave-top" viewBox="0 0 178 40" height="40" preserveAspectRatio="none" aria-hidden="true">
    <path d="M0 0 L178 0 L178 18 C120 36 60 6 0 26Z" fill="var(--blue-light)" opacity=".6"/>
  </svg>
  <div class="brand on-blue"><span class="brand-dot"></span><span class="brand-name">Harbor<br>Portable Scanning</span></div>
  <p class="card-web">www.harborportablescanninginc.com</p>
</section>

<!-- envelope -->
<section class="sheet envelope" aria-label="Envelope">
  <svg class="wave wave-top" viewBox="0 0 482 64" height="64" preserveAspectRatio="none" aria-hidden="true">
    <path d="M0 0 L482 0 L482 58 C340 30 200 64 0 44Z" fill="var(--blue-light)"/>
    <path d="M0 0 L482 0 L482 48 C330 22 190 56 0 36Z" fill="var(--blue)"/>
    <path d="M0 0 L482 0 L482 34 C320 14 180 44 0 24Z" fill="var(--blue-dark)"/>
  </svg>
  <p class="envelope-return">P.O. Box 527 Ashwick NJ 08176</p>
  <div class="brand"><span class="brand-dot"></span><span class="brand-name">Harbor<br>Portable Scanning</span></div>
  <p class="envelope-address">P.O. Box 527 Ashwick NJ 08176<br>Phone: 856-555-0142<br>Email: Info@harborportablescanninginc.com</p>
  <div class="envelope-window"></div>
</section>

<!-- notepad -->
<section class="sheet notepad" aria-label="Notepad">
  <div class="brand"><span class="brand-dot"></span><span class="brand-name">Harbor<br>Portable Scanning</span></div>
  <div class="note-lines"></div>
  <p class="note-date">Date:</p>
  <svg class="wave wave-bottom" viewBox="0 0 170 44" height="44" preserveAspectRatio="none" aria-hidden="true">
    <path d="M0 14 C50 0 110 26 170 6 L170 44 L0 44Z" fill="var(--blue-light)"/>
    <path d="M0 24 C60 10 110 34 170 16 L170 44 L0 44Z" fill="var(--blue)"/>
    <path d="M0 34 C60 24 120 42 170 28 L170 44 L0 44Z" fill="var(--blue-dark)"/>
  </svg>
</section>

</body>
</html>
```